Brightwater Court Services needs a business card

I need a business card design for a new company
For the last 10 years I have ran a tennis management company called Silver Hollow Racquet (www.silverhollowracquet.com)
The new company - Brightwater Court Services (BCS) will replace SHRA starting this winter
The goal of BCS will be to expand our operations into new clubs as well and a revenue stream from existing clubs with courtlinkhub.net
We plan to go regional in 2014 and then look outward from there

Target Market(s)

small to medium sized tennis facilities both public and private
Our market are the clubs - not the players
This includes private clubs, municipalities, recreation assc, etc

Industry/Entity Type

Business

Requirements
Must have
• Dale Huxley
• President
• 555-284-1937 Office
• 555-419-5062 Cell
• dhuxley@brightwatercourtservices.com
• www.brightwatercourtservices.com
Nice to have
• One of the unique benefits to a company joining BCS will be integration into our web based club software service - Courtlinkhub.net
• We have developed this turnkey service for small to medium sized clubs and re the exclusive providers of it
Should not have
• address or state

```html
<!DOCTYPE html>
<html lang="en">
<head>
<meta charset="utf-8">
<title>Brightwater Court Services — Card Back</title>
<link rel="stylesheet" href="https://fonts.googleapis.com/css2?family=Source+Sans+3:wght@300;400&display=swap">
<style>
  :root {
    --paper: #ffffff;
    --sun: #fccf0a;
    --sun-soft: rgba(252, 207, 10, 0);
    --teal: #5f9ca1;
    --trim: #3a3a3a;
  }
  html, body {
    margin: 0;
    padding: 0;
    overflow: hidden;
    background: var(--paper);
  }
  .card-back {
    position: relative;
    width: 680px;
    height: 1200px;
    overflow: hidden;
    background: var(--paper);
  }
  .sun-field {
    position: absolute;
    left: 60px;
    top: 60px;
    width: 560px;
    height: 1079px;
    background:
      linear-gradient(to bottom,
        var(--sun) 0%,
        var(--sun) 26%,
        var(--sun-soft) 50%,
        var(--sun-soft) 78%,
        var(--sun) 100%);
  }
  .trim-marks {
    position: absolute;
    inset: 0;
  }
  .trim-mark { stroke: var(--trim); stroke-width: 1.6; fill: none; }
  .web-address {
    position: absolute;
    left: 327px;
    top: 731px;
    margin: 0;
    transform: translate(-50%, -50%) rotate(-90deg);
    white-space: nowrap;
    font-family: "Source Sans 3", sans-serif;
    font-weight: 300;
    font-size: 39px;
    letter-spacing: 0.6px;
    color: var(--teal);
  }
</style>
</head>
<body>
  <main class="card-back">
    <div class="sun-field" role="img" aria-label="Decorative yellow curved bands framing the card, large at the top and small at the bottom"></div>
    <svg class="trim-marks" width="680" height="1200" viewBox="0 0 680 1200" aria-hidden="true">
      <line class="trim-mark" x1="78" y1="0" x2="78" y2="45"/>
      <line class="trim-mark" x1="0" y1="78" x2="45" y2="78"/>
      <line class="trim-mark" x1="597" y1="0" x2="597" y2="45"/>
      <line class="trim-mark" x1="635" y1="78" x2="680" y2="78"/>
      <line class="trim-mark" x1="78" y1="1155" x2="78" y2="1200"/>
      <line class="trim-mark" x1="0" y1="1121" x2="45" y2="1121"/>
      <line class="trim-mark" x1="597" y1="1155" x2="597" y2="1200"/>
      <line class="trim-mark" x1="635" y1="1121" x2="680" y2="1121"/>
    </svg>
    <p class="web-address">www.brightwatercourtservices.com</p>
  </main>
</body>
</html>
```